Business Card Design Project - IT Company

Kestrafield Information Technology Solutions
We are an Information Technology Company. We provide computer services to commercial companies. We would like a new card full color front and back with bleeding edge.
We have a logo that you can use or if you want to come up with a new logo that is fine too.
Our colors are mostly Maroon and black but be creative.
Sample Information
Brent R Okafor
4812 W Saguaro Ridge Drive
Suite 410
Phoenix, AZ 85029
O: 602.914.2037
C: 602.468.1290
24/7: 888.914.2037
bokafor@kestrafield.example
www.kestrafield.example
Target Market(s)
Business of all sizes
Industry/Entity Type
Computer
Requirements
Must have
- Bleeding edge
full color on both sides

```html
<!DOCTYPE html>
<html lang="en">
<head>
<meta charset="utf-8">
<title>Kestrafield Business Card</title>
<link rel="stylesheet" href="https://fonts.googleapis.com/css2?family=Open+Sans:wght@400;600;700&family=Cormorant+Garamond:wght@500;700&display=swap">
<style>
  :root {
    --maroon: #c1272d;
    --graphite: #636466;
    --slate: #6d6e71;
    --paper: #ffffff;
    --backdrop: #e7e5e2;
  }
  * { margin: 0; padding: 0; box-sizing: border-box; }
  html, body { width: 1200px; height: 900px; overflow: hidden; }
  body { background: var(--backdrop); font-family: "Open Sans", Arial, sans-serif; }
  .canvas { position: relative; width: 1200px; height: 900px; }

  .card { position: absolute; width: 740px; overflow: hidden; }
  .card--front { left: 16px; top: 44px; height: 388px; background: var(--maroon); }
  .card--back { left: 448px; top: 456px; height: 420px; background: var(--graphite); }

  .front-curves { position: absolute; left: 0; top: 0; width: 740px; height: 388px; }

  .brand { position: absolute; text-align: center; }
  .brand__name {
    font-family: "Cormorant Garamond", Georgia, serif;
    font-weight: 500; line-height: 1; white-space: nowrap;
  }
  .brand__tagline {
    font-family: "Cormorant Garamond", Georgia, serif;
    font-weight: 700; line-height: 1.1; white-space: nowrap;
  }
  .card--front .brand { left: 150px; top: 12px; width: 440px; }
  .card--front .brand__name { font-size: 42px; letter-spacing: 7px; color: var(--slate); }
  .card--front .brand__tagline { font-size: 19px; color: var(--slate); margin-top: 2px; }

  .holder {
    position: absolute; left: 150px; width: 440px; top: 92px;
    text-align: center; font-weight: 700; font-size: 25px; color: var(--slate);
  }

  .contact { position: absolute; color: var(--paper); white-space: nowrap; }
  .contact__address { left: 48px; top: 230px; font-size: 18px; }
  .contact__phones, .contact__web { font-size: 15px; line-height: 1.55; }
  .contact__phones { left: 48px; top: 266px; }
  .contact__web { left: 424px; top: 272px; }
  .contact__label { font-weight: 700; }

  .card--back .brand { left: 0; width: 740px; top: 168px; }
  .card--back .brand__name { font-size: 54px; color: var(--paper); letter-spacing: 9px; }
  .card--back .brand__tagline { font-size: 22px; color: var(--paper); margin-top: 6px; }
</style>
</head>
<body>
<main class="canvas">

  <section class="card card--front" aria-label="Card front">
    <svg class="front-curves" viewBox="0 0 740 388" aria-hidden="true">
      <path fill="var(--paper)" d="M0,0 H740 V16 C650,120 470,150 340,148 C200,146 80,100 0,56 Z"/>
      <path fill="var(--slate)" d="M0,56 C80,100 200,146 340,148 C470,150 650,120 740,16 V30 C660,150 480,170 340,164 C190,160 80,112 0,82 Z"/>
      <path fill="none" stroke="var(--paper)" stroke-width="3" d="M0,98 C90,134 200,174 340,180 C490,186 660,150 740,42"/>
    </svg>

    <div class="brand">
      <div class="brand__name">KESTRAFIELD</div>
      <div class="brand__tagline">Information Technology Solutions</div>
    </div>

    <h1 class="holder">Brent R Okafor</h1>

    <p class="contact contact__address">4812 W Saguaro Ridge Drive Suite 410, Phoenix, AZ 85029</p>
    <p class="contact contact__phones">
      <span class="contact__label">O:</span> 602.914.2037<br>
      <span class="contact__label">C:</span> 602.468.1290<br>
      <span class="contact__label">24/7:</span> 888.914.2037
    </p>
    <p class="contact contact__web">
      <span class="contact__label">E:</span> bokafor@kestrafield.example<br>
      www.kestrafield.example
    </p>
  </section>

  <section class="card card--back" aria-label="Card back">
    <div class="brand">
      <div class="brand__name">KESTRAFIELD</div>
      <div class="brand__tagline">Information Technology Solutions</div>
    </div>
  </section>

</main>
</body>
</html>
```